Bluff Marigold

Need a site for a cbd dispensary texas theme. We sell all federal and legal hemp products

Target Market(s)

Cbd and other hemp derivatives

Industry/Entity Type

Hemp derivatives

Coding

Coded - Design and coding required

Number of Pages Required

3 page

Font styles to use
Sans Serif

Colors
0094D4
00A9DD
6FCCEA
C7EBF8
E9F6FB

Requirements
Must have
• Integration for bigcommerce shopping
Nice to have
• Easy layout for shopping

```html
<!DOCTYPE html>
<html lang="en">
<head>
<meta charset="utf-8">
<title>Bluff Marigold</title>
<link href="https://fonts.googleapis.com/css2?family=Poppins:ital,wght@0,400;0,500;0,600;0,700;1,400;1,500&display=swap" rel="stylesheet">
<style>
:root{
  --blue:#0094D4;
  --blue-2:#00A9DD;
  --blue-3:#6FCCEA;
  --blue-4:#C7EBF8;
  --blue-5:#E9F6FB;
  --ink:#111;
  --text:#333;
  --muted:#666;
  --card:#f3f3f3;
  --star:#f5b301;
  --footer:#141414;
}
*{box-sizing:border-box;margin:0;padding:0}
html,body{width:1200px;height:4669px;overflow:hidden}
body{font-family:'Poppins',sans-serif;color:var(--text);background:#fff;position:relative}
section,header,footer,.topbar{position:relative;width:1200px}
.wrap{position:absolute;left:100px;width:1000px}
.section-title{position:absolute;left:0;width:1200px;text-align:center;font-weight:600;font-size:36px;color:var(--ink);letter-spacing:.3px}

.topbar{height:35px;background:var(--blue);color:#fff;font-size:12px;font-weight:500;display:flex;align-items:center;justify-content:center;gap:8px}
.nav{height:70px;background:#fff;z-index:5}
.nav a{position:absolute;top:27px;font-size:14px;font-weight:600;color:var(--ink);text-decoration:none;letter-spacing:.3px}
.logo-cap{position:absolute;left:495px;top:-10px;width:210px;height:120px;background:#fff;border-radius:0 0 105px 105px;display:flex;align-items:center;justify-content:center}
.logo-cap span{font-weight:700;font-size:24px;color:var(--blue);text-align:center;line-height:1.05;margin-top:-8px}
.nav-icons{position:absolute;right:100px;top:24px;display:flex;gap:12px}
.hero{height:602px;overflow:hidden}
.hero-photo{position:absolute;inset:0;background:linear-gradient(100deg,#1c2a1a 0%,#2f3d2a 35%,#5a4a3c 60%,#8a6a55 78%,#3b2f28 100%)}
.hero h1{position:absolute;left:109px;top:200px;font-size:50px;font-weight:600;color:#fff;letter-spacing:.5px}
.hero p{position:absolute;left:109px;top:268px;width:420px;font-size:16px;line-height:26px;color:#fff}
.btn{display:inline-flex;align-items:center;justify-content:center;background:var(--blue);color:#fff;font-weight:600;font-size:14px;text-decoration:none;letter-spacing:.3px}
.hero .btn{position:absolute;left:109px;top:348px;width:150px;height:41px}
.hero-arrow{position:absolute;top:282px}
.dots{position:absolute;display:flex;gap:9px}
.dots i{width:11px;height:11px;border-radius:50%;border:1.5px solid #fff;display:block}
.dots i.on{background:#fff}

.categories{height:558px;background:var(--blue-5)}
.cat-grid{top:163px;display:flex;gap:16px}
.cat{width:238px;height:299px;background:#fff;position:relative;box-shadow:0 2px 8px rgba(0,0,0,.06)}
.cat .ph{height:224px}
.cat .ic{position:absolute;left:84px;top:187px;width:70px;height:70px;border-radius:50%;background:#fff;display:flex;align-items:center;justify-content:center}
.cat .lbl{position:absolute;left:0;right:0;top:258px;text-align:center;font-weight:600;font-size:18px;color:var(--ink)}

.products{height:640px}
.prod-grid{top:158px;display:flex;gap:17px}
.prod{width:237px;text-align:center}
.prod .ph{height:281px;background:var(--card);position:relative;display:flex;align-items:center;justify-content:center}
.bottle{border-radius:8px 8px 6px 6px}
.badge{position:absolute;right:12px;top:13px;width:34px;height:34px;border-radius:50%;background:var(--blue-2);color:#fff;font-size:10px;font-weight:600;display:flex;align-items:center;justify-content:center}
.stars{margin-top:16px;font-size:12px;color:var(--star);letter-spacing:1px}
.stars span{color:var(--muted);font-size:11px;letter-spacing:0;margin-left:4px}
.pname{margin-top:6px;font-size:13px;font-weight:600;line-height:22px;color:var(--ink)}
.price{margin-top:6px;font-size:15px;font-weight:600;color:var(--ink)}
.price s{color:var(--muted);font-weight:400;margin-right:4px}
.slide-arrow{position:absolute;width:40px;height:40px;border-radius:50%;border:1.8px solid var(--ink);display:flex;align-items:center;justify-content:center;background:#fff}

.story{height:524px;background:var(--blue-5)}
.story .ph-back{position:absolute;left:107px;top:76px;width:270px;height:312px;background:linear-gradient(160deg,#c8b79b,#8aa36a 45%,#c78d84)}
.story .blue-sq{position:absolute;left:377px;top:98px;width:93px;height:60px;background:var(--blue-3)}
.story .ph-front{position:absolute;left:256px;top:158px;width:311px;height:290px;background:linear-gradient(180deg,#2b84b5 0%,#3d8fc0 40%,#d8d0c4 55%,#9a6a3f 75%,#7a4e2c 100%)}
.story .eyebrow{position:absolute;left:663px;top:94px;font-size:11px;font-weight:600;color:var(--blue);letter-spacing:.3px}
.story h2{position:absolute;left:663px;top:106px;font-size:36px;font-weight:600;color:var(--ink)}
.story .rule{position:absolute;left:663px;top:160px;width:80px;height:3px;background:var(--blue)}
.story p{position:absolute;left:663px;top:192px;width:438px;font-size:13px;line-height:25px;color:var(--text)}
.story .btn{position:absolute;left:663px;top:383px;width:151px;height:44px}

.testimonials{height:507px;background:linear-gradient(180deg,var(--blue-2),var(--blue));overflow:hidden}
.testimonials .texture{position:absolute;inset:0;background:repeating-linear-gradient(90deg,rgba(255,255,255,.05) 0 120px,rgba(0,0,0,.04) 120px 240px)}
.testimonials .section-title{color:#fff;top:120px}
.quote{position:absolute;top:203px;width:426px;height:181px;background:#fff;padding:24px 20px 0 41px}
.quote p{font-style:italic;font-size:13px;line-height:25.5px;color:var(--ink)}
.quote b{display:block;margin-top:10px;font-size:14px;font-weight:600;color:var(--ink)}
.qmark{position:absolute;top:262px;width:58px;height:58px;border-radius:50%;background:var(--blue);border:4px solid #fff;color:#fff;font-size:48px;font-weight:700;display:flex;align-items:center;justify-content:center;line-height:1;padding-top:18px}

.blog{height:617px}
.blog-grid{top:160px;display:flex;gap:15px}
.post{width:324px}
.post .ph{height:203px}
.post h3{margin-top:22px;font-size:15px;font-weight:600;line-height:22px;color:var(--ink);white-space:nowrap}
.post p{margin-top:8px;font-size:11px;line-height:19px;color:var(--muted)}
.post a{display:inline-flex;align-items:center;gap:6px;margin-top:14px;font-size:11px;font-weight:600;color:var(--blue);text-decoration:none}

.newsletter{height:103px;background:var(--blue)}
.nl-icon{position:absolute;left:101px;top:20px;width:63px;height:63px;border-radius:50%;border:2px solid #fff;display:flex;align-items:center;justify-content:center}
.nl-text{position:absolute;left:182px;top:28px;color:#fff;font-size:15px;font-weight:500;line-height:24px}
.nl-input{position:absolute;left:613px;top:28px;width:318px;height:49px;background:#fff;display:flex;align-items:center;padding-left:14px;font-size:13px;color:#777}
.nl-btn{position:absolute;left:943px;top:28px;width:155px;height:49px;border:2px solid #fff;background:var(--blue);color:#fff;font-weight:600;font-size:15px;display:flex;align-items:center;justify-content:center}

.footer{height:364px;background:var(--footer);color:#fff}
.f-logo{position:absolute;left:100px;top:58px;font-weight:700;font-size:40px;line-height:1.05;color:#fff}
.socials{position:absolute;left:100px;top:238px;display:flex;gap:14px}
.socials i{width:44px;height:44px;border-radius:50%;border:2px solid #fff;display:block}
.f-col{position:absolute;top:68px}
.f-col h4{font-size:15px;font-weight:600;letter-spacing:.3px;margin-bottom:14px}
.f-col li{list-style:none;font-size:13px;line-height:27.5px;color:#eee}
.contact li{display:flex;gap:10px;line-height:20px;margin-bottom:10px}
.f-rule{position:absolute;left:100px;top:286px;width:1000px;height:1px;background:#333}
.copyright{position:absolute;left:100px;top:290px;height:44px;display:flex;align-items:center;font-size:12px;color:#ddd}
.pay{position:absolute;right:100px;top:303px;display:flex;gap:7px}
.pay i{width:32px;height:20px;border-radius:3px;display:block}
</style>
</head>
<body>

<div class="topbar">
  <svg width="18" height="14" viewBox="0 0 18 14" fill="none" stroke="#fff" stroke-width="1.4"><rect x="1" y="2" width="10" height="8"/><path d="M11 5h4l2 3v2h-6"/><circle cx="5" cy="11.5" r="1.5" fill="#0094D4"/><circle cx="14" cy="11.5" r="1.5" fill="#0094D4"/></svg>
  Shipping &amp; Returns Are Always Free From Our Place To Yours. 😊
</div>

<header class="nav">
  <a style="left:100px" href="#">HOME</a>
  <a style="left:180px" href="#">PRODUCTS</a>
  <a style="left:297px" href="#">ABOUT</a>
  <a style="left:376px" href="#">FAQS</a>
  <div class="logo-cap"><span>Bluff<br>Marigold</span></div>
  <a style="left:779px" href="#">WHAT'S CBD?</a>
  <a style="left:917px" href="#">HELP</a>
  <div class="nav-icons">
    <svg width="20" height="20" viewBox="0 0 20 20" fill="none" stroke="#111" stroke-width="1.6"><circle cx="8" cy="8" r="6"/><path d="M12.5 12.5 18 18"/></svg>
    <svg width="20" height="20" viewBox="0 0 20 20" fill="none" stroke="#111" stroke-width="1.6"><path d="M10 17 3 10a4 4 0 0 1 7-5 4 4 0 0 1 7 5z"/></svg>
    <svg width="20" height="20" viewBox="0 0 20 20" fill="none" stroke="#111" stroke-width="1.6"><circle cx="10" cy="6" r="4"/><path d="M2 19c1-5 4-7 8-7s7 2 8 7"/></svg>
    <svg width="22" height="20" viewBox="0 0 22 20" fill="none" stroke="#111" stroke-width="1.6"><path d="M2 6h14l-1 12H3z"/><path d="M6 6a3 3 0 0 1 6 0"/><circle cx="17" cy="13" r="4.5" fill="#0094D4" stroke="none"/></svg>
  </div>
</header>

<section class="hero">
  <div class="hero-photo" role="img" aria-label="Woman holding a dropper bottle of hemp oil in front of dark green hemp leaves"></div>
  <h1>BLUFF MARIGOLD</h1>
  <p>Lorem ipsum dolor sit amet, consectetur adipiscing elit, sed do eiusmod tempor</p>
  <a class="btn" href="#">SHOP NOW</a>
  <svg class="hero-arrow" style="left:62px" width="20" height="40" viewBox="0 0 20 40" fill="none" stroke="#fff" stroke-width="2"><path d="M18 2 2 20l16 18"/></svg>
  <svg class="hero-arrow" style="left:1119px" width="20" height="40" viewBox="0 0 20 40" fill="none" stroke="#fff" stroke-width="2"><path d="M2 2l16 18L2 38"/></svg>
  <div class="dots" style="left:561px;top:554px"><i></i><i class="on"></i><i></i><i></i></div>
</section>

<section class="categories">
  <h2 class="section-title" style="top:82px">SHOP CATEGORIES</h2>
  <div class="wrap cat-grid">
    <div class="cat">
      <div class="ph" role="img" aria-label="Massage therapist hands on a client's back" style="background:linear-gradient(160deg,#e9c9b0,#c68f6c)"></div>
      <div class="ic"><svg width="38" height="38" viewBox="0 0 38 38" fill="none" stroke="#0094D4" stroke-width="1.8"><circle cx="19" cy="7" r="4"/><path d="M5 20h28M8 20v12M30 20v12M12 20c2-5 5-7 7-7s5 2 7 7"/></svg></div>
      <div class="lbl">Relief</div>
    </div>
    <div class="cat">
      <div class="ph" role="img" aria-label="Person meditating on a terrace above a tropical town" style="background:linear-gradient(180deg,#9fc0d6,#b9c8ae 45%,#6f7b5a 75%,#9b8d7a)"></div>
      <div class="ic"><svg width="38" height="38" viewBox="0 0 38 38" fill="none" stroke="#0094D4" stroke-width="1.8"><circle cx="19" cy="7" r="4"/><path d="M19 12v10M11 17l8 3 8-3M6 30c4-4 9-6 13-6s9 2 13 6H6z"/></svg></div>
      <div class="lbl">Wellness</div>
    </div>
    <div class="cat">
      <div class="ph" role="img" aria-label="Woman applying a facial oil with a dropper against a pink backdrop" style="background:linear-gradient(160deg,#f1c5c8,#e7a9ae 50%,#7a4a36)"></div>
      <div class="ic"><svg width="38" height="38" viewBox="0 0 38 38" fill="none" stroke="#0094D4" stroke-width="1.8"><ellipse cx="19" cy="18" rx="9" ry="12"/><path d="M10 14c3-6 15-6 18 0M7 8l5 4M31 8l-5 4"/></svg></div>
      <div class="lbl">Beauty</div>
    </div>
    <div class="cat">
      <div class="ph" role="img" aria-label="Dog running through waves on a beach" style="background:linear-gradient(180deg,#a9c7dd,#5f8fb3 55%,#dbe6ec)"></div>
      <div class="ic"><svg width="38" height="38" viewBox="0 0 38 38" fill="none" stroke="#0094D4" stroke-width="1.8"><ellipse cx="19" cy="26" rx="7" ry="6"/><circle cx="9" cy="17" r="3"/><circle cx="29" cy="17" r="3"/><circle cx="14" cy="9" r="3"/><circle cx="24" cy="9" r="3"/></svg></div>
      <div class="lbl">Pets</div>
    </div>
  </div>
</section>

<section class="products">
  <h2 class="section-title" style="top:85px">FEATURED PRODUCTS</h2>
  <div class="slide-arrow" style="left:47px;top:281px"><svg width="12" height="14" viewBox="0 0 12 14" fill="none" stroke="#111" stroke-width="1.8"><path d="M9 1 3 7l6 6"/></svg></div>
  <div class="slide-arrow" style="left:1109px;top:281px"><svg width="12" height="14" viewBox="0 0 12 14" fill="none" stroke="#111" stroke-width="1.8"><path d="M3 1l6 6-6 6"/></svg></div>
  <div class="wrap prod-grid">
    <div class="prod">
      <div class="ph"><div class="bottle" role="img" aria-label="Amber jar of hemp capsules" style="width:120px;height:170px;background:linear-gradient(90deg,#3a1d0c,#8a4a1c 50%,#3a1d0c)"></div></div>
      <div class="stars">★★★★★<span>(115)</span></div>
      <div class="pname">Finibus Bonorum et Malorum<br>perspiciatis unde</div>
      <div class="price"><s>$43.00</s>$38.00</div>
    </div>
    <div class="prod">
      <div class="ph"><div class="bottle" role="img" aria-label="Black dropper bottle of hemp oil" style="width:70px;height:210px;background:linear-gradient(90deg,#111,#3a3a3a 50%,#111)"></div><div class="badge">-12%</div></div>
      <div class="stars">★★★★★<span>(115)</span></div>
      <div class="pname">Finibus Bonorum et Malorum<br>perspiciatis unde</div>
      <div class="price"><s>$43.00</s>$38.00</div>
    </div>
    <div class="prod">
      <div class="ph"><div class="bottle" role="img" aria-label="Boxed jar of hemp soft gels" style="width:170px;height:150px;background:linear-gradient(90deg,#7a5a3c,#b88f66 40%,#1f1f1f 60%,#2d2d2d)"></div></div>
      <div class="stars">★★★★★<span>(115)</span></div>
      <div class="pname">Finibus Bonorum et Malorum<br>perspiciatis unde</div>
      <div class="price"><s>$43.00</s>$38.00</div>
    </div>
    <div class="prod">
      <div class="ph"><div class="bottle" role="img" aria-label="Green glass dropper bottle of hemp oil" style="width:75px;height:200px;background:linear-gradient(90deg,#1f4a3a,#4d8a72 50%,#1f4a3a)"></div><div class="badge">-12%</div></div>
      <div class="stars">★★★★★<span>(115)</span></div>
      <div class="pname">Finibus Bonorum et Malorum<br>perspiciatis unde</div>
      <div class="price"><s>$43.00</s>$38.00</div>
    </div>
  </div>
</section>

<section class="story">
  <div class="ph-back" role="img" aria-label="Woman in a sun hat among hemp plants"></div>
  <div class="blue-sq"></div>
  <div class="ph-front" role="img" aria-label="Dispensary shelves stocked with hemp products under a blue wall"></div>
  <div class="eyebrow">ABOUT BLUFF MARIGOLD</div>
  <h2>OUR STORY</h2>
  <div class="rule"></div>
  <p>Lorem ipsum dolor sit amet, consectetur adipiscing elit, sed do eiusmod tempor incididunt ut labore et dolorega aliqua. Quis ipsum suspendisse ultrices gravida. Risuomviverra maecenas accumsan lacus vel facilisis. Lorem ipsor sit amet, consectetur adipiscing elit, sed do eiusmod tempor incidiunt bore et dolore magna aliqua. Quis ipsum suspendisse ultrices gravida. Risus commodo viverra maecenas accumsan lacus vel facilisis.</p>
  <a class="btn" href="#">LEARN MORE</a>
</section>

<section class="products" style="height:649px">
  <h2 class="section-title" style="top:85px">BEST SELLER</h2>
  <div class="slide-arrow" style="left:47px;top:283px"><svg width="12" height="14" viewBox="0 0 12 14" fill="none" stroke="#111" stroke-width="1.8"><path d="M9 1 3 7l6 6"/></svg></div>
  <div class="slide-arrow" style="left:1109px;top:283px"><svg width="12" height="14" viewBox="0 0 12 14" fill="none" stroke="#111" stroke-width="1.8"><path d="M3 1l6 6-6 6"/></svg></div>
  <div class="wrap prod-grid" style="top:160px">
    <div class="prod">
      <div class="ph"><div class="bottle" role="img" aria-label="Boxed jar of hemp soft gels" style="width:170px;height:150px;background:linear-gradient(90deg,#7a5a3c,#b88f66 40%,#1f1f1f 60%,#2d2d2d)"></div></div>
      <div class="stars">★★★★★<span>(115)</span></div>
      <div class="pname">Finibus Bonorum et Malorum<br>perspiciatis unde</div>
      <div class="price"><s>$43.00</s>$38.00</div>
    </div>
    <div class="prod">
      <div class="ph"><div class="bottle" role="img" aria-label="Amber dropper bottle of hemp oil" style="width:70px;height:200px;background:linear-gradient(90deg,#5a2a08,#b0641c 50%,#5a2a08)"></div><div class="badge">-12%</div></div>
      <div class="stars">★★★★★<span>(115)</span></div>
      <div class="pname">Finibus Bonorum et Malorum<br>perspiciatis unde</div>
      <div class="price"><s>$43.00</s>$38.00</div>
    </div>
    <div class="prod">
      <div class="ph"><div class="bottle" role="img" aria-label="Amber bottle of hemp gummies with a white label" style="width:110px;height:190px;background:linear-gradient(180deg,#c8501a 0 18%,#f4f4f4 18% 72%,#3a3a3a 72%)"></div></div>
      <div class="stars">★★★★★<span>(115)</span></div>
      <div class="pname">Finibus Bonorum et Malorum<br>perspiciatis unde</div>
      <div class="price"><s>$43.00</s>$38.00</div>
    </div>
    <div class="prod">
      <div class="ph"><div class="bottle" role="img" aria-label="Boxed amber dropper bottle of hemp oil" style="width:170px;height:180px;background:linear-gradient(90deg,#7a5a3c,#b88f66 45%,#9a5a1c 60%,#c47a2c)"></div><div class="badge">-12%</div></div>
      <div class="stars">★★★★★<span>(115)</span></div>
      <div class="pname">Finibus Bonorum et Malorum<br>perspiciatis unde</div>
      <div class="price"><s>$43.00</s>$38.00</div>
    </div>
  </div>
</section>

<section class="testimonials">
  <div class="texture" role="img" aria-label="Blue-tinted shelves of hemp product packaging"></div>
  <h2 class="section-title">CLIENT TESTIMONIALS</h2>
  <svg style="position:absolute;left:86px;top:278px" width="16" height="32" viewBox="0 0 16 32" fill="none" stroke="#fff" stroke-width="2"><path d="M14 2 2 16l12 14"/></svg>
  <svg style="position:absolute;left:1098px;top:278px" width="16" height="32" viewBox="0 0 16 32" fill="none" stroke="#fff" stroke-width="2"><path d="M2 2l12 14L2 30"/></svg>
  <div class="quote" style="left:156px">
    <p>Lorem ipsum dolor sit amet, consectetur adipiscing elit,<br>sed do eiusmod tempor incididunt ut lab magna aliqua.<br>Quis ipsum suspendisse ultrices gravida. Rus commodo<br>viverra maecenas accumsan</p>
    <b>- JOHN DOE</b>
  </div>
  <div class="qmark" style="left:127px">“</div>
  <div class="quote" style="left:644px">
    <p>Lorem ipsum dolor sit amet, consectetur adipiscing elit,<br>sed do eiusmod tempor incididunt ut lab magna aliqua.<br>Quis ipsum suspendisse ultrices gravida. Rus commodo<br>viverra maecenas accumsan</p>
    <b>- JOHN DOE</b>
  </div>
  <div class="qmark" style="left:615px">“</div>
  <div class="dots" style="left:565px;top:415px"><i class="on" style="width:9px;height:9px"></i><i style="width:9px;height:9px;background:rgba(255,255,255,.6)"></i><i style="width:9px;height:9px;background:rgba(255,255,255,.6)"></i><i style="width:9px;height:9px;background:rgba(255,255,255,.6)"></i><i style="width:9px;height:9px;background:rgba(255,255,255,.6)"></i></div>
</section>

<section class="blog">
  <h2 class="section-title" style="top:85px">LATEST BLOG</h2>
  <div class="wrap blog-grid">
    <article class="post">
      <div class="ph" role="img" aria-label="Hands holding a glass of hemp oil among leaves and bottles" style="background:linear-gradient(150deg,#e6c9a0,#d4aa78 50%,#8aa35a)"></div>
      <h3>Lorem ipsum dolor sit amctetur<br>adipiscing elit, sed do eiusmod tempor</h3>
      <p>Lorem ipsum dolor sit amet, consectetur adipiiing elit, sed do eiusmod tempor incididunt ut labore et dolore magna aliqua. Quis ipsum suspendisse</p>
      <a href="#">READ MORE <svg width="14" height="8" viewBox="0 0 14 8" fill="none" stroke="#0094D4" stroke-width="1.6"><path d="M0 4h12M9 1l3 3-3 3"/></svg></a>
    </article>
    <article class="post">
      <div class="ph" role="img" aria-label="Bottle of hemp oil surrounded by green hemp leaves" style="background:linear-gradient(150deg,#eef0ea,#b7cf9a 50%,#4f8a3a)"></div>
      <h3>Lorem ipsum dolor sit amctetur<br>adipiscing elit, sed do eiusmod tempor</h3>
      <p>Lorem ipsum dolor sit amet, consectetur adipiiing elit, sed do eiusmod tempor incididunt ut labore et dolore magna aliqua. Quis ipsum suspendisse</p>
      <a href="#">READ MORE <svg width="14" height="8" viewBox="0 0 14 8" fill="none" stroke="#0094D4" stroke-width="1.6"><path d="M0 4h12M9 1l3 3-3 3"/></svg></a>
    </article>
    <article class="post">
      <div class="ph" role="img" aria-label="Dropper bottle beside dried hemp flower on a dark background" style="background:linear-gradient(160deg,#2a1e16,#5a3a22 50%,#6e7a3a)"></div>
      <h3>Lorem ipsum dolor sit amctetur<br>adipiscing elit, sed do eiusmod tempor</h3>
      <p>Lorem ipsum dolor sit amet, consectetur adipiiing elit, sed do eiusmod tempor incididunt ut labore et dolore magna aliqua. Quis ipsum suspendisse</p>
      <a href="#">READ MORE <svg width="14" height="8" viewBox="0 0 14 8" fill="none" stroke="#0094D4" stroke-width="1.6"><path d="M0 4h12M9 1l3 3-3 3"/></svg></a>
    </article>
  </div>
</section>

<section class="newsletter">
  <div class="nl-icon"><svg width="30" height="22" viewBox="0 0 30 22" fill="none" stroke="#fff" stroke-width="1.8"><rect x="1" y="1" width="28" height="20" rx="2"/><path d="M1 2l14 11L29 2"/></svg></div>
  <div class="nl-text">Sign up today to receive exclusive updates<br>on the latest deals we have to offer. must be 18+</div>
  <div class="nl-input">Enter your email here</div>
  <div class="nl-btn">SUBSCRIBE</div>
</section>

<footer class="footer">
  <div class="f-logo">Bluff<br>Marigold</div>
  <div class="socials"><i></i><i></i><i></i><i></i></div>
  <div class="f-col" style="left:466px">
    <h4>QUICK LINKS</h4>
    <ul><li>Home</li><li>About Us</li><li>Categories</li><li>Deals</li><li>Articles</li><li>Contact Us</li></ul>
  </div>
  <div class="f-col" style="left:685px">
    <h4>SUPPORT</h4>
    <ul><li>Help Center</li><li>Shipping &amp; Warranty</li><li>Privacy Policy</li><li>FAQ's</li></ul>
  </div>
  <div class="f-col contact" style="left:910px">
    <h4>CONTACT INFO</h4>
    <ul>
      <li><svg width="12" height="16" viewBox="0 0 12 16"><path d="M6 0a6 6 0 0 1 6 6c0 4-6 10-6 10S0 10 0 6a6 6 0 0 1 6-6z" fill="#0094D4"/><circle cx="6" cy="6" r="2" fill="#141414"/></svg><span>4821 Pecan Hollow Lane<br>USA 73301</span></li>
      <li><svg width="13" height="13" viewBox="0 0 13 13"><path d="M3 0l2 3-1.5 1.5a8 8 0 0 0 5 5L10 8l3 2-1.5 3C6 13 0 7 0 1.5z" fill="#0094D4"/></svg><span>Phone:<br>512 555 0147</span></li>
      <li><svg width="14" height="11" viewBox="0 0 14 11"><rect width="14" height="11" rx="1" fill="#0094D4"/><path d="M1 1l6 5 6-5" fill="none" stroke="#141414" stroke-width="1.2"/></svg><span>Email:<br>hello@bluffmarigold.com</span></li>
    </ul>
  </div>
  <div class="f-rule"></div>
  <div class="copyright">Copyright © 2021 Bluff Marigold. All rights reserved.</div>
  <div class="pay"><i style="background:#2a63b8"></i><i style="background:#e9edf3"></i><i style="background:#3a3a3a"></i><i style="background:#1a3fa0"></i><i style="background:#4a8fd8"></i><i style="background:#f2c12e"></i></div>
</footer>

</body>
</html>
```